VelaCure Wellness Business Cards

I am looking to have luxury business cards made for my IV Therapy and Wellness business.
Updates

Target Market(s)

Health and Wellness professionals

Industry/Entity Type

MedSpa

Contact Information for Business Card

Tobin Haverly, MSN, RN, CCRN Tobin@velacurewellness.com (916) 582-3179 QR code to website www.velacurewellness.com

```html
<!DOCTYPE html>
<html lang="en">
<head>
<meta charset="UTF-8">
<title>VelaCure Wellness Business Card</title>
<link rel="stylesheet" href="https://fonts.googleapis.com/css2?family=Playfair+Display:wght@500;700&family=Poppins:wght@400;500&display=swap">
<style>
  :root {
    --stage: #1c1c20;
    --card: #1f2124;
    --card-edge: #2a2c30;
    --silver: #b9bbbe;
    --gold: #c9a233;
    --ink-light: #f2f2f2;
  }
  * { box-sizing: border-box; margin: 0; padding: 0; }
  html, body {
    width: 1200px; height: 800px; overflow: hidden;
    background: var(--stage);
  }
  .stage {
    width: 1200px; height: 800px;
    display: flex; align-items: center; justify-content: center; gap: 40px;
  }
  .card {
    position: relative;
    width: 540px; height: 309px;
    background: var(--card);
    border: 1px solid var(--card-edge);
    border-radius: 18px;
    overflow: hidden;
  }
  .card-front {
    display: flex; align-items: center; justify-content: center;
  }
  .front-brand {
    font-family: "Playfair Display", serif;
    font-weight: 500;
    font-size: 38px;
    color: var(--silver);
    letter-spacing: 0.5px;
  }
  .brand-block {
    position: absolute; left: 36px; top: 132px;
    width: 200px;
  }
  .back-brand {
    font-family: "Playfair Display", serif;
    font-weight: 500;
    font-size: 27px;
    line-height: 1.15;
    color: var(--gold);
  }
  .divider {
    position: absolute; left: 248px; top: 62px;
    width: 1px; height: 132px;
    background: var(--gold);
  }
  .contact-block {
    position: absolute; left: 268px; top: 58px; right: 16px;
  }
  .person-name {
    font-family: "Playfair Display", serif;
    font-weight: 700;
    font-size: 21px;
    color: var(--gold);
  }
  .person-title {
    font-family: "Poppins", sans-serif;
    font-size: 13px;
    color: var(--ink-light);
    margin-bottom: 14px;
  }
  .contact-list { list-style: none; }
  .contact-item {
    display: flex; align-items: center; gap: 10px;
    font-family: "Poppins", sans-serif;
    font-size: 12.5px;
    color: var(--ink-light);
    line-height: 22px;
    white-space: nowrap;
  }
  .contact-icon { width: 13px; height: 13px; flex: none; }
  .address {
    position: absolute; left: 36px; right: 30px; bottom: 28px;
    font-family: "Poppins", sans-serif;
    font-size: 13px;
    color: var(--ink-light);
  }
</style>
</head>
<body>
<main class="stage">
  <section class="card card-front" aria-label="Card front">
    <h1 class="front-brand">VelaCure Wellness</h1>
  </section>

  <section class="card card-back" aria-label="Card back">
    <div class="brand-block">
      <p class="back-brand">VelaCure Wellness</p>
    </div>
    <div class="divider"></div>
    <div class="contact-block">
      <p class="person-name">Tobin Haverly</p>
      <p class="person-title">MSN, RN, CCRN</p>
      <ul class="contact-list">
        <li class="contact-item">
          <svg class="contact-icon" viewBox="0 0 14 14"><rect x="2" y="1" width="10" height="12" rx="1.5" fill="none" stroke="var(--gold)" stroke-width="1.6"/></svg>
          (916) 582-3179
        </li>
        <li class="contact-item">
          <svg class="contact-icon" viewBox="0 0 14 14"><rect x="1" y="3" width="12" height="8" fill="var(--gold)"/><path d="M1 3 L7 8 L13 3" fill="none" stroke="var(--card)" stroke-width="1.2"/></svg>
          Tobin@velacurewellness.com
        </li>
        <li class="contact-item">
          <svg class="contact-icon" viewBox="0 0 14 14"><circle cx="7" cy="7" r="6" fill="none" stroke="var(--gold)" stroke-width="1.4"/><path d="M1 7 H13 M7 1 C4 4 4 10 7 13 M7 1 C10 4 10 10 7 13" fill="none" stroke="var(--gold)" stroke-width="1"/></svg>
          www.velacurewellness.com
        </li>
      </ul>
    </div>
    <p class="address">PO Box 7812, Elm Street, 5th Lane, United States</p>
  </section>
</main>
</body>
</html>
```